Souvenir and Health Food Products

We need a website designed for a Wholesaler & Distributor of Australia Made Souvenir & Health Food products. Our range includes many of Australia's leading brands: Willow's Cottage, Southern Meadow Essentials, Pebble & Ferne, Vanto Cosmetics, Drelona, K T Leathergoods, Trestin Leathergoods, Brekker's Salt & Tallowick Honey.

Design will be converted into a Dot Net Nuke skin and containers so needs to be compatible.

Needs to show off their products and be easy to navigate.

Would like a nice clean and corporate look.
Updates

Hi Everyone

All design concepts are with my client who has been extremely busy....hoping to get feedback from them this week.

Cheers
Mabel

Target Market(s)

Target market are retail shops looking to stock their products

Industry/Entity Type

Health

Number of Pages Required

2 pages

Requirements
Must have
• Proposed Site Map
• Home
• About Us
• Products
• Ordering
• Contact Us

• To be included in homepage design concept:

• Large area for a flash banner of rotating images on homepage
• Logo and Phone number in header for every page 07 5000 3172
• Some welcome text
• Some icons will need to be designed - Register for our newsletter and Contact Us
• Product category list on homepage – thumbnail image/name of category (click through)

• Product categories to use are:
• (allow for up to 15)
• • Willow’s Cottage (use p1000321/jpg)

• • Jojoba Oil (use TFP_0121.jpg))

• • Southern Meadow Essentials (use TFP_0077.jpg)

• Could you create a separate content page to show how products will look on category page with each product having a thumbnail image, description and Enquire now button.
Should not have
• No shopping cart or ecommerce needed

```html
<!DOCTYPE html>
<html lang="en">
<head>
<meta charset="utf-8">
<title>Corrawind Trading – Wholesale Souvenir &amp; Health Food Products</title>
<link rel="stylesheet" href="https://fonts.googleapis.com/css2?family=Arimo:wght@400;700&display=swap">
<style>
  :root {
    --sky-top: #3f8fc7;
    --sky-mid: #8cc0e2;
    --sky-pale: #f2f7fb;
    --panel: #f5f5f5;
    --panel-border: #d6d9dc;
    --link: #1b8ac4;
    --ink: #222629;
    --body-text: #555a5e;
    --rule: #a9d3e8;
    --caption-bg: #aad8e1;
    --mail-top: #4aa3d2;
    --mail-bottom: #86c3e3;
    --thumb-border: #c9ccce;
    --footer-band: #8fc3e3;
  }
  * { box-sizing: border-box; margin: 0; padding: 0; }
  html, body { width: 1200px; height: 1128px; overflow: hidden; }
  body {
    position: relative;
    font-family: "Arimo", Arial, sans-serif;
    color: var(--ink);
    background: linear-gradient(to bottom,
      var(--sky-top) 0px, var(--sky-mid) 200px, var(--sky-pale) 420px,
      #ffffff 700px, #ffffff 1060px, var(--footer-band) 1128px);
  }
  a { text-decoration: none; color: var(--link); }

  /* Header */
  .brand { position: absolute; left: 72px; top: 62px; display: flex; align-items: center; gap: 14px; }
  .brand-mark { width: 52px; height: 52px; border-radius: 50%; background: #1c6fa8; }
  .brand-name { font-size: 36px; font-weight: 700; color: #1b1f22; letter-spacing: 1px; }
  .call-today { position: absolute; right: 84px; top: 74px; font-size: 17px; color: #1b1f22; }
  .call-today .phone { font-size: 27px; margin-left: 6px; }

  /* Main panel */
  .panel {
    position: absolute; left: 48px; top: 126px; width: 1104px; height: 924px;
    background: var(--panel); border: 1px solid var(--panel-border); border-radius: 24px;
  }
  .column-divider { position: absolute; left: 347px; top: 162px; height: 852px; border-left: 1px dashed #b9bcbf; }

  /* Sidebar navigation */
  .side-nav { position: absolute; left: 84px; top: 175px; width: 234px; list-style: none; }
  .side-nav li { height: 60px; border-bottom: 1px dashed var(--rule); display: flex; align-items: flex-end; padding-bottom: 11px; font-size: 19px; line-height: 22px; }
  .side-nav li.ordering { height: 65px; padding-bottom: 13px; }
  .side-nav li:first-child a { color: var(--ink); }
  .side-nav li.contact { height: 53px; border-bottom: none; gap: 18px; padding-bottom: 8px; }
  .mail-icon { width: 38px; height: 24px; margin-bottom: 2px; }

  /* Mailing list */
  .mailing {
    position: absolute; left: 84px; top: 475px; width: 234px; height: 180px;
    background: linear-gradient(to bottom, var(--mail-top), var(--mail-bottom));
    border-radius: 0 0 14px 14px; color: #fff;
  }
  .mailing h3 { position: absolute; left: 24px; top: 20px; font-size: 19px; font-weight: 400; color: #0f2a3a; }
  .mailing .field { position: absolute; left: 24px; display: flex; align-items: center; gap: 12px; font-size: 15px; }
  .mailing .field span { width: 132px; height: 29px; background: #fff; border: 1px solid #d2e6f1; }
  .mailing .name-field { top: 60px; }
  .mailing .email-field { top: 96px; }
  .mailing .subscribe { position: absolute; left: 0; width: 100%; top: 136px; text-align: center; font-size: 18px; }

  /* News */
  .news-title { position: absolute; left: 84px; top: 692px; width: 234px; font-size: 19px; font-weight: 400; color: var(--link); padding-bottom: 8px; border-bottom: 1px dashed var(--rule); }
  .news-list { position: absolute; left: 86px; top: 745px; width: 210px; list-style: none; font-size: 15px; line-height: 18px; color: var(--body-text); }
  .news-list li { position: relative; padding-left: 16px; margin-bottom: 18px; }
  .news-list li::before { content: ""; position: absolute; left: 0; top: 5px; width: 5px; height: 5px; background: var(--link); }
  .more-news { position: absolute; left: 200px; width: 125px; text-align: right; top: 1001px; font-size: 13px; letter-spacing: .5px; }

  /* Banner */
  .banner { position: absolute; left: 348px; top: 162px; width: 768px; height: 372px; }
  .banner-photo { position: absolute; left: 0; top: 0; width: 492px; height: 312px;
    background: radial-gradient(ellipse at 50% 55%, #e9eef0 0%, #d9e2e4 45%, #c7d7d6 100%); }
  .banner-caption { position: absolute; left: 492px; top: 0; width: 276px; height: 312px; background: var(--caption-bg); border-radius: 0 12px 0 0; padding: 22px 24px; }
  .banner-caption h2 { font-size: 19px; font-weight: 400; color: var(--ink); margin-bottom: 12px; }
  .banner-caption p { width: 214px; font-size: 15.5px; line-height: 21.5px; color: #5a6468; }
  .banner-caption .links { position: absolute; left: 24px; top: 210px; font-size: 16.5px; line-height: 29px; }
  .banner-bar { position: absolute; left: 0; top: 312px; width: 768px; height: 60px;
    background: linear-gradient(to right, #9ccfe2 0%, #c9e6ef 50%, #9fd2e2 100%); }
  .pager { position: absolute; left: 12px; top: 12px; display: flex; gap: 12px; list-style: none; }
  .pager li { width: 36px; height: 36px; border: 1px solid rgba(255,255,255,.8); color: #5f8ea3; font-size: 17px; display: flex; align-items: center; justify-content: center; }
  .pager li.current { background: rgba(255,255,255,.55); color: var(--ink); }
  .search { position: absolute; right: 12px; top: 12px; width: 252px; height: 36px; border: 1px solid rgba(255,255,255,.9); font-size: 16px; color: #4e5a60; display: flex; align-items: center; justify-content: flex-end; padding-right: 12px; }

  /* Browse products */
  .browse-title { position: absolute; left: 384px; top: 566px; font-size: 19px; font-weight: 400; }
  .view-all { position: absolute; right: 84px; top: 569px; font-size: 13px; letter-spacing: .5px; }
  .category-grid { position: absolute; left: 377px; top: 595px; display: grid; grid-template-columns: repeat(5, 132px); grid-auto-rows: 150px; column-gap: 21.6px; list-style: none; }
  .category { text-align: center; }
  .category .thumb { display: block; width: 118px; height: 96px; margin: 0 auto 8px; border: 1px solid var(--thumb-border); }
  .category .caption { display: block; font-size: 14px; line-height: 16px; color: var(--link); white-space: nowrap; }
  .thumb.jars { background: linear-gradient(to bottom, #f5f7f4 0%, #5c7a64 50%, #c9b28a 100%); }
  .thumb.boxes { background: linear-gradient(to right, #a6d34f 0%, #e9f2f3 50%, #d33a3a 100%); }
  .thumb.soaps { background: linear-gradient(to bottom, #f4f1e6 0%, #98a36a 55%, #6f7c3e 100%); }
  .thumb.oils { background: linear-gradient(to right, #fafafa 0%, #b22a3a 45%, #d6a23a 100%); }
  .thumb.aloe { background: linear-gradient(to bottom, #f7faf8 0%, #7cab8d 55%, #e7efee 100%); }

  /* Footer */
  .footer-nav { position: absolute; left: 0; width: 1200px; top: 1072px; text-align: center; font-size: 14px; color: #2b2f32; }
  .footer-nav a { color: #2b2f32; }
  .footer-nav .sep { margin: 0 13px; }
  .copyright { position: absolute; left: 0; width: 1200px; top: 1103px; text-align: center; font-size: 12px; color: #2b2f32; }
</style>
</head>
<body>
  <header>
    <div class="brand"><span class="brand-mark"></span><span class="brand-name">CORRAWIND TRADING</span></div>
    <div class="call-today">CALL TODAY <span class="phone">07 5000 3172</span></div>
  </header>

  <div class="panel"></div>
  <div class="column-divider"></div>

  <nav>
    <ul class="side-nav">
      <li><a href="#">Welcome</a></li>
      <li><a href="#">About Corrawind</a></li>
      <li><a href="#">Product Catalog</a></li>
      <li class="ordering"><a href="#">Ordering Information</a></li>
      <li class="contact"><a href="#">Contact Us</a>
        <svg class="mail-icon" viewBox="0 0 38 24" aria-hidden="true">
          <rect x="1" y="1" width="36" height="22" fill="#eef1f3" stroke="#b7bfc4"/>
          <polyline points="1,1 19,14 37,1" fill="none" stroke="#b7bfc4"/>
        </svg>
      </li>
    </ul>
  </nav>

  <section class="mailing">
    <h3>Join our mailing list:</h3>
    <div class="field name-field"><span></span>Name</div>
    <div class="field email-field"><span></span>Email</div>
    <div class="subscribe">Subscribe</div>
  </section>

  <h3 class="news-title">Latest News</h3>
  <ul class="news-list">
    <li>Suspendisse vel turpis ut dolor ornare interdum. Curabitur vel libero. Nullam facilisis placerat risus.</li>
    <li>Suspendisse vel turpis ut dolor ornare interdum.</li>
    <li>Suspendisse vel turpis ut dolor ornare interdum. Curabitur vel libero. Nullam facilisis placerat risus.</li>
  </ul>
  <a class="more-news" href="#">MORE NEWS »</a>

  <section class="banner">
    <div class="banner-photo" role="img" aria-label="Group of health food and cosmetic products: supplement tubs, propolis jars, jojoba cream and oil bottles"></div>
    <div class="banner-caption">
      <h2>Image Title</h2>
      <p>Image description to go here. Suspendisse vel turpis ut dolor ornare interdum. Curabitur vel libero. Nullam facilisis placerat risus.</p>
      <div class="links"><a href="#">Product Details »</a><br><a href="#">View our Product Catalog »</a></div>
    </div>
    <div class="banner-bar">
      <ol class="pager"><li class="current">1</li><li>2</li><li>3</li><li>4</li></ol>
      <div class="search">Enter a keyword or phrase</div>
    </div>
  </section>

  <h2 class="browse-title">Browse Products</h2>
  <a class="view-all" href="#">VIEW ALL PRODUCTS »</a>
  <ul class="category-grid">
    <li class="category"><span class="thumb jars" role="img" aria-label="Supplement jars"></span><span class="caption">Category Title Here</span></li>
    <li class="category"><span class="thumb boxes" role="img" aria-label="Assorted health products"></span><span class="caption">Category Title Here</span></li>
    <li class="category"><span class="thumb soaps" role="img" aria-label="Natural soaps and oils"></span><span class="caption">Category Title Here</span></li>
    <li class="category"><span class="thumb oils" role="img" aria-label="Cosmetic oil bottles"></span><span class="caption">Category Title Here</span></li>
    <li class="category"><span class="thumb aloe" role="img" aria-label="Aloe plant with skincare tube"></span><span class="caption">Category Title Here</span></li>
    <li class="category"><span class="thumb aloe" role="img" aria-label="Aloe plant with skincare tube"></span><span class="caption">Category Title Here</span></li>
    <li class="category"><span class="thumb oils" role="img" aria-label="Cosmetic oil bottles"></span><span class="caption">Category Title Here</span></li>
    <li class="category"><span class="thumb jars" role="img" aria-label="Supplement jars"></span><span class="caption">Category Title Here</span></li>
    <li class="category"><span class="thumb boxes" role="img" aria-label="Assorted health products"></span><span class="caption">Category Title Here</span></li>
    <li class="category"><span class="thumb soaps" role="img" aria-label="Natural soaps and oils"></span><span class="caption">Category Title Here</span></li>
    <li class="category"><span class="thumb jars" role="img" aria-label="Supplement jars"></span><span class="caption">Category Title Here</span></li>
    <li class="category"><span class="thumb boxes" role="img" aria-label="Assorted health products"></span><span class="caption">Category Title Here</span></li>
    <li class="category"><span class="thumb aloe" role="img" aria-label="Aloe plant with skincare tube"></span><span class="caption">Category Title Here</span></li>
    <li class="category"><span class="thumb soaps" role="img" aria-label="Natural soaps and oils"></span><span class="caption">Category Title Here</span></li>
    <li class="category"><span class="thumb oils" role="img" aria-label="Cosmetic oil bottles"></span><span class="caption">Category Title Here</span></li>
  </ul>

  <footer>
    <nav class="footer-nav">
      <a href="#">Welcome</a><span class="sep">|</span><a href="#">About Corrawind</a><span class="sep">|</span><a href="#">Product Catalog</a><span class="sep">|</span><a href="#">FAQs</a><span class="sep">|</span><a href="#">Contact Us</a><span class="sep">|</span><a href="#">Terms of Use</a><span class="sep">|</span><a href="#">Privacy Policy</a>
    </nav>
    <p class="copyright">© Copyright 2009, Corrawind Trading, Inc.&nbsp; Registration #123456788.&nbsp; All rights reserved under law.</p>
  </footer>
</body>
</html>
```